Talon Microchips PowerPoint Master Slide Deck Design

This is a 2-phase project to design a slide deck for a semiconductor company in the Silicon Valley. The design budget will be increased with each phase.
The slide deck will need to have one version with a dark background for presentations and a second version with a white background. Otherwise, the slides will be the same. I anticipate we will need a total of 10 slides, but that number may change.
The first phase will be to design a Title and a Title and Content slide.
- The Title Slide is the first slide of the deck. It should include the presentation title, the presenter's name and date of presentation
- The Title and Content slide should include a title and content with bullet points and up to 2 additional sub-bullets
- The Title and Content slide should have a footer that includes the slide #, Talon Microchips Confidential, and the logo. This footer will be on every slide except the Title Slide
The first two slides will serve as the format for the remaining ~8 slides:
-Header and Content Text (1, 2, 4 column)
-Header and Content Image (bar chart, pie chart, tables)
-Break
-Title only
-Closing (Talon logo only)
Our slides contain a lot of content so a clean and simple design is best.
Both phases will need to include pre-set color options for
-Text and Lines
-Shadows
-Bullets and sub-bullets (including shapes, ex. circle, slash, square, etc.)
-Bar charts, pie charts, tables
Samples of our collateral are attached. Logo files are also attached

```html
<!DOCTYPE html>
<html lang="en">
<head>
<meta charset="utf-8">
<title>Talon Microchips – Slide Deck</title>
<link rel="stylesheet" href="https://fonts.googleapis.com/css2?family=Montserrat:wght@400;500;600;700;800&family=Arimo:wght@400;700&display=swap">
<style>
:root{
  --stage:#4a4a4a;
  --paper:#ffffff;
  --brand-blue:#0a3cf0;
  --title-blue:#0a3de8;
  --sky:#00aaf0;
  --bar-light:#00b4f5;
  --bar-dark:#0a3cf0;
  --ink:#111111;
  --body:#444444;
  --grid:#dddddd;
}
*{margin:0;padding:0;box-sizing:border-box}
html,body{width:1200px;height:1058px;overflow:hidden;background:var(--stage)}
body{position:relative;font-family:"Montserrat",sans-serif;color:var(--ink)}
.slide{position:absolute;width:561px;height:315px;background:var(--paper);overflow:hidden}
.slide-title{left:30px;top:35px}
.slide-agenda{left:615px;top:35px}
.slide-chart{left:30px;top:369px}
.slide-profile{left:610px;top:367px}
.slide-about{left:30px;top:703px}
.slide-closing{left:615px;top:707px}

.footer-band{position:absolute;left:0;top:0;width:561px;height:315px}
.footer-note{position:absolute;left:30px;top:293px;font-size:5.6px;color:#fff;font-weight:500}
.footer-brand{position:absolute;left:414px;top:283px;display:flex;align-items:center;gap:5px;color:#fff;font-size:10px;font-weight:600;white-space:nowrap}
.footer-brand .mark{width:8px;height:8px;border-radius:50%;background:#fff}
.page-no{position:absolute;left:535px;top:302px;font-size:4.6px;color:#fff}

.heading{position:absolute;font-weight:800;color:var(--title-blue);font-size:15px;letter-spacing:.2px;white-space:nowrap}

/* title slide */
.hero-art{position:absolute;left:0;top:0;width:330px;height:315px}
.top-brand{position:absolute;left:478px;top:14px;display:flex;align-items:center;gap:4px;color:var(--title-blue);font-size:8.5px;font-weight:600;white-space:nowrap}
.top-brand .mark{width:7px;height:7px;border-radius:50%;background:var(--title-blue)}
.welcome{position:absolute;left:332px;top:118px;font-size:9px;font-weight:700;color:var(--title-blue)}
.deck-title{position:absolute;left:332px;top:132px;font-size:19px;line-height:24px;font-weight:800;color:var(--sky)}
.presenter{position:absolute;left:332px;top:186px;display:flex;gap:10px;font-size:9.5px;color:var(--title-blue)}
.presenter span{display:flex;align-items:center;gap:2px}

/* agenda */
.topic{position:absolute;white-space:nowrap}
.topic h3{display:flex;align-items:center;gap:3px;font-size:10.5px;font-weight:600;color:var(--sky)}
.topic h3::before{content:"";width:8px;height:8px;border-radius:50%;background:var(--sky)}
.topic ul{list-style:none;margin:7px 0 0 23px}
.topic li{display:flex;align-items:center;gap:2px;font-size:6.3px;font-weight:600;height:13.5px}
.topic li::before{content:"";width:5px;height:5px;border-radius:50%;background:var(--ink)}

/* chart */
.chart{position:absolute;left:0;top:0;width:345px;height:265px;font-family:"Arimo",sans-serif}
.chart-notes{position:absolute;left:339px;top:54px;width:212px;font-size:6.3px;line-height:10.6px;color:var(--body)}
.chart-notes ul{list-style:none;margin-top:4px}
.chart-notes li{display:flex;gap:2px;margin-bottom:4.8px}
.chart-notes li svg{flex:none;margin-top:2px}

/* profile */
.profile-copy{position:absolute;left:31px;top:52px;width:524px;font-size:7.3px;line-height:11.7px;color:var(--body)}
.profile-copy p+p{margin-top:3.5px}

/* about */
.about-copy{position:absolute;left:33px;top:119px;width:208px;font-size:6.3px;line-height:10.6px;color:var(--body)}
.about-art{position:absolute;left:316px;top:34px;width:206px;height:206px}

/* closing */
.closing-brand{position:absolute;left:0;top:112px;width:561px;display:flex;align-items:center;justify-content:center;gap:14px;color:var(--brand-blue);font-size:40px;font-weight:700;white-space:nowrap}
.closing-brand .mark{width:28px;height:28px;border-radius:50%;background:var(--brand-blue)}
</style>
</head>
<body>

<!-- 01 Title -->
<section class="slide slide-title">
  <svg class="hero-art" viewBox="0 0 330 315" role="img" aria-label="Photo of automated chip assembly machinery over a circuit board">
    <defs>
      <linearGradient id="heroFill" x1="0" y1="0" x2="1" y2="1">
        <stop offset="0" stop-color="#3c5066"/>
        <stop offset=".5" stop-color="#3f8d96"/>
        <stop offset="1" stop-color="#1f5a62"/>
      </linearGradient>
    </defs>
    <path d="M0,0 H222 C330,55 332,255 224,315 H0 Z" fill="var(--brand-blue)"/>
    <path d="M0,0 H204 C312,60 310,258 200,315 H0 Z" fill="url(#heroFill)"/>
  </svg>
  <div class="top-brand"><span class="mark"></span>Talon Microchips</div>
  <p class="welcome">WELCOME TO</p>
  <h1 class="deck-title">TALON<br>MICROCHIPS</h1>
  <div class="presenter">
    <span><svg width="7" height="8" viewBox="0 0 7 8"><circle cx="3.5" cy="2" r="2" fill="var(--title-blue)"/><path d="M0,8 C0,4.5 7,4.5 7,8 Z" fill="var(--title-blue)"/></svg>Mara Quinn</span>
    <span><svg width="8" height="8" viewBox="0 0 8 8"><rect x=".5" y="1.5" width="7" height="6" fill="none" stroke="var(--title-blue)"/><rect x=".5" y="1.5" width="7" height="1.6" fill="var(--title-blue)"/><path d="M2,0v2M6,0v2" stroke="var(--title-blue)"/></svg>13-12-2023</span>
  </div>
</section>

<!-- 02 What we do -->
<section class="slide slide-agenda">
  <svg class="footer-band" viewBox="0 0 561 315" aria-hidden="true"><path d="M0,229 Q0,272 50,272 H505 Q552,272 561,315 H0 Z" fill="var(--brand-blue)"/></svg>
  <h2 class="heading" style="left:31px;top:20px">WHAT WE DO</h2>
  <div class="topic" style="left:33px;top:51px"><h3>Lorem ipsum dolor sit amet, consectetur</h3><ul><li>Lorem ipsum dolor sit amet, consectetur sed do</li><li>Lorem ipsum dolor sit amet, consectetur sed do</li><li>Lorem ipsum dolor sit amet, consectetur sed do</li></ul></div>
  <div class="topic" style="left:33px;top:124px"><h3>Lorem ipsum dolor sit amet, consectetur</h3><ul><li>Lorem ipsum dolor sit amet, consectetur sed do</li><li>Lorem ipsum dolor sit amet, consectetur sed do</li><li>Lorem ipsum dolor sit amet, consectetur sed do</li></ul></div>
  <div class="topic" style="left:33px;top:197px"><h3>Lorem ipsum dolor sit amet, consectetur</h3><ul><li>Lorem ipsum dolor sit amet, consectetur sed do</li><li>Lorem ipsum dolor sit amet, consectetur sed do</li><li>Lorem ipsum dolor sit amet, consectetur sed do</li></ul></div>
  <div class="topic" style="left:292px;top:51px"><h3>Lorem ipsum dolor sit amet, consectetur</h3><ul><li>Lorem ipsum dolor sit amet, consectetur sed do</li><li>Lorem ipsum dolor sit amet, consectetur sed do</li><li>Lorem ipsum dolor sit amet, consectetur sed do</li></ul></div>
  <div class="topic" style="left:292px;top:124px"><h3>Lorem ipsum dolor sit amet, consectetur</h3><ul><li>Lorem ipsum dolor sit amet, consectetur sed do</li><li>Lorem ipsum dolor sit amet, consectetur sed do</li><li>Lorem ipsum dolor sit amet, consectetur sed do</li></ul></div>
  <div class="topic" style="left:292px;top:197px"><h3>Lorem ipsum dolor sit amet, consectetur</h3><ul><li>Lorem ipsum dolor sit amet, consectetur sed do</li><li>Lorem ipsum dolor sit amet, consectetur sed do</li><li>Lorem ipsum dolor sit amet, consectetur sed do</li></ul></div>
  <p class="footer-note">Talon Microchips Confidential</p>
  <div class="footer-brand"><span class="mark"></span>Talon Microchips</div>
  <span class="page-no">02</span>
</section>

<!-- 03 Bar chart -->
<section class="slide slide-chart">
  <svg class="footer-band" viewBox="0 0 561 315" aria-hidden="true"><path d="M0,229 Q0,272 50,272 H505 Q552,272 561,315 H0 Z" fill="var(--brand-blue)"/></svg>
  <h2 class="heading" style="left:31px;top:21px">BAR CHART</h2>
  <svg class="chart" viewBox="0 0 345 265" aria-label="Bar chart by weekday">
    <g stroke="var(--grid)" stroke-width=".6">
      <line x1="34" y1="65" x2="316" y2="65"/><line x1="34" y1="94.3" x2="316" y2="94.3"/><line x1="34" y1="123.7" x2="316" y2="123.7"/><line x1="34" y1="153" x2="316" y2="153"/><line x1="34" y1="182.4" x2="316" y2="182.4"/><line x1="34" y1="211.7" x2="316" y2="211.7"/><line x1="34" y1="241" x2="316" y2="241"/>
      <line x1="34" y1="65" x2="34" y2="241"/><line x1="74.3" y1="65" x2="74.3" y2="241"/><line x1="114.6" y1="65" x2="114.6" y2="241"/><line x1="154.9" y1="65" x2="154.9" y2="241"/><line x1="195.1" y1="65" x2="195.1" y2="241"/><line x1="235.4" y1="65" x2="235.4" y2="241"/><line x1="275.7" y1="65" x2="275.7" y2="241"/><line x1="316" y1="65" x2="316" y2="241"/>
    </g>
    <g font-size="6" fill="#222" text-anchor="end">
      <text x="29" y="67">120</text><text x="29" y="96">100</text><text x="29" y="126">80</text><text x="29" y="155">60</text><text x="29" y="184">40</text><text x="29" y="214">20</text><text x="29" y="243">0</text>
    </g>
    <g fill="var(--bar-light)">
      <rect x="44.6" y="94.3" width="7.6" height="146.7"/><rect x="84.9" y="108.9" width="7.6" height="132.1"/><rect x="125.2" y="167.7" width="7.6" height="73.3"/><rect x="165.5" y="94.3" width="7.6" height="146.7"/><rect x="205.7" y="94.3" width="7.6" height="146.7"/><rect x="246" y="153" width="7.6" height="88"/><rect x="286.3" y="167.7" width="7.6" height="73.3"/>
    </g>
    <g fill="var(--bar-dark)">
      <rect x="56.9" y="108.9" width="7.6" height="132.1"/><rect x="97.2" y="123.7" width="7.6" height="117.3"/><rect x="137.5" y="94.3" width="7.6" height="146.7"/><rect x="177.8" y="153" width="7.6" height="88"/><rect x="218" y="108.9" width="7.6" height="132.1"/><rect x="258.3" y="131" width="7.6" height="110"/><rect x="298.6" y="94.3" width="7.6" height="146.7"/>
    </g>
    <g font-size="5.8" fill="#222" text-anchor="middle">
      <text x="48.4" y="91">100</text><text x="60.7" y="105.6">90</text>
      <text x="88.7" y="105.6">90</text><text x="101" y="120.4">80</text>
      <text x="129" y="164.4">50</text><text x="141.3" y="91">100</text>
      <text x="169.3" y="91">100</text><text x="181.6" y="149.7">60</text>
      <text x="209.5" y="91">100</text><text x="221.8" y="105.6">90</text>
      <text x="249.8" y="149.7">60</text><text x="262.1" y="127.7">75</text>
      <text x="290.1" y="164.4">50</text><text x="302.4" y="91">100</text>
    </g>
    <g font-size="6.2" font-weight="700" fill="#222" text-anchor="middle">
      <text x="54" y="252">Sun</text><text x="94" y="252">Mon</text><text x="134" y="252">Tue</text><text x="175" y="252">Wed</text><text x="215" y="252">Thu</text><text x="253" y="252">Fri</text><text x="292" y="252">Sat</text>
    </g>
  </svg>
  <div class="chart-notes">
    <p>Lorem ipsum dolor sit amet, consectetur adipiscing elit, sed do eiusmod tempor incididunt ut labore et dolore magna aliqua. Ut enim ad minim veniam, quis nostrud exercitation ullamco laboris nisi ut aliquip ex ea commodo consequat. Duis aute irure dolor in reprehenderit in voluptate velit esse cillum dolore eu fugiat nulla pariatur.</p>
    <ul>
      <li><svg width="6" height="6" viewBox="0 0 6 6"><circle cx="3" cy="3" r="3" fill="var(--brand-blue)"/><path d="M1.5,3H4M3,1.8L4.3,3L3,4.2" stroke="#fff" stroke-width=".8" fill="none"/></svg><span>Sed ut perspiciatis unde omnis iste natus error sit voluptatem accusantium doloremque laudantium dicta sunt explicabo.</span></li>
      <li><svg width="6" height="6" viewBox="0 0 6 6"><circle cx="3" cy="3" r="3" fill="var(--brand-blue)"/><path d="M1.5,3H4M3,1.8L4.3,3L3,4.2" stroke="#fff" stroke-width=".8" fill="none"/></svg><span>Sed ut perspiciatis unde omnis iste natus error sit voluptatem accusantium doloremque laudantium dicta sunt explicabo.</span></li>
      <li><svg width="6" height="6" viewBox="0 0 6 6"><circle cx="3" cy="3" r="3" fill="var(--brand-blue)"/><path d="M1.5,3H4M3,1.8L4.3,3L3,4.2" stroke="#fff" stroke-width=".8" fill="none"/></svg><span>Sed ut perspiciatis unde omnis iste natus error sit voluptatem accusantium doloremque laudantium dicta sunt explicabo.</span></li>
      <li><svg width="6" height="6" viewBox="0 0 6 6"><circle cx="3" cy="3" r="3" fill="var(--brand-blue)"/><path d="M1.5,3H4M3,1.8L4.3,3L3,4.2" stroke="#fff" stroke-width=".8" fill="none"/></svg><span>Sed ut perspiciatis unde omnis iste natus error sit voluptatem accusantium doloremque laudantium dicta sunt explicabo.</span></li>
      <li><svg width="6" height="6" viewBox="0 0 6 6"><circle cx="3" cy="3" r="3" fill="var(--brand-blue)"/><path d="M1.5,3H4M3,1.8L4.3,3L3,4.2" stroke="#fff" stroke-width=".8" fill="none"/></svg><span>Sed ut perspiciatis unde omnis iste natus error sit voluptatem accusantium doloremque laudantium dicta sunt explicabo.</span></li>
    </ul>
  </div>
  <p class="footer-note">Talon Microchips Confidential</p>
  <div class="footer-brand"><span class="mark"></span>Talon Microchips</div>
  <span class="page-no">03</span>
</section>

<!-- 04 Who we are -->
<section class="slide slide-profile">
  <svg class="footer-band" viewBox="0 0 561 315" aria-hidden="true"><path d="M0,229 Q0,272 50,272 H505 Q552,272 561,315 H0 Z" fill="var(--brand-blue)"/></svg>
  <h2 class="heading" style="left:31px;top:20px">WHO WE ARE</h2>
  <div class="profile-copy">
    <p>Lorem ipsum dolor sit amet, consectetur adipiscing elit, sed do eiusmod tempor incididunt ut labore et dolore magna aliqua. Ut enim ad minim veniam, quis nostrud exercitation ullamco laboris nisi ut aliquip ex ea commodo consequat. Duis aute irure dolor in reprehenderit in voluptate velit esse cillum dolore eu fugiat nulla pariatur.</p>
    <p>Sed ut perspiciatis unde omnis iste natus error sit voluptatem accusantium doloremque laudantium, totam rem aperiam, eaque ipsa quae ab illo inventore veritatis et quasi architecto beatae vitae dicta sunt explicabo. Nemo enim ipsam voluptatem quia voluptas sit aspernatur aut odit aut fugit, sed quia consequuntur magni dolores eos qui ratione voluptatem sequi nesciunt. Neque porro quisquam est, qui dolorem ipsum quia dolor sit amet, consectetur, adipisci velit, sed quia non numquam eius modi tempora incidunt ut labore et dolore magnam aliquam quaerat voluptatem.</p>
    <p>Ut enim ad minima veniam, quis nostrum exercitationem ullam corporis suscipit laboriosam, nisi ut aliquid ex ea commodi consequatur? Quis autem vel eum iure reprehenderit qui in ea voluptate velit esse quam nihil molestiae consequatur, vel illum qui dolorem eum fugiat quo voluptas nulla pariatur. Sed ut perspiciatis unde omnis iste natus error sit voluptatem accusantium doloremque laudantium, totam rem aperiam, eaque ipsa quae ab illo inventore veritatis et quasi architecto beatae vitae dicta sunt explicabo. Nemo enim ipsam voluptatem quia voluptas sit aspernatur aut odit aut fugit, sed quia consequuntur magni dolores eos qui ratione voluptatem sequi nesciunt. Neque porro quisquam est, qui dolorem ipsum quia dolor sit amet, consectetur, adipisci velit, sed quia non numquam eius modi tempora incidunt ut labore et dolore magnam aliquam quaerat voluptatem. Sed ut perspiciatis unde omnis iste natus error sit voluptatem accusantium doloremque laudantium, totam rem aperiam, eaque ipsa quae ab illo inventore veritatis et quasi architecto beatae vitae dicta sunt explicabo.</p>
  </div>
  <p class="footer-note">Talon Microchips Confidential</p>
  <div class="footer-brand"><span class="mark"></span>Talon Microchips</div>
  <span class="page-no">04</span>
</section>

<!-- 05 About us -->
<section class="slide slide-about">
  <svg class="footer-band" viewBox="0 0 561 315" aria-hidden="true"><path d="M0,229 Q0,272 50,272 H505 Q552,272 561,315 H0 Z" fill="var(--brand-blue)"/></svg>
  <h2 class="heading" style="left:33px;top:92px">ABOUT US</h2>
  <p class="about-copy">Lorem ipsum dolor sit amet, consectetur adipiscing elit, sed do eiusmod tempor incididunt ut labore et dolore magna aliqua. Ut enim ad minim veniam, quis nostrud exercitation ullamco laboris nisi ut aliquip ex ea commodo consequat. Duis aute irure dolor in reprehenderit in voluptate velit esse cillum dolore eu fugiat nulla pariatur.</p>
  <svg class="about-art" viewBox="0 0 206 206" role="img" aria-label="Illustration of a glowing processor chip on a blue circuit board">
    <defs>
      <radialGradient id="chipGlow" cx=".5" cy=".55" r=".6">
        <stop offset="0" stop-color="#2f7df5"/>
        <stop offset=".6" stop-color="#1c45d6"/>
        <stop offset="1" stop-color="#10249a"/>
      </radialGradient>
    </defs>
    <circle cx="103" cy="103" r="103" fill="url(#chipGlow)"/>
  </svg>
  <p class="footer-note">Talon Microchips Confidential</p>
  <div class="footer-brand"><span class="mark"></span>Talon Microchips</div>
  <span class="page-no">05</span>
</section>

<!-- 06 Closing -->
<section class="slide slide-closing">
  <svg class="footer-band" viewBox="0 0 561 315" aria-hidden="true"><path d="M0,229 Q0,272 50,272 H505 Q552,272 561,315 H0 Z" fill="var(--brand-blue)"/></svg>
  <div class="closing-brand"><span class="mark"></span>Talon Microchips</div>
  <p class="footer-note">Talon Microchips Confidential</p>
  <div class="footer-brand"><span class="mark"></span>Talon Microchips</div>
  <span class="page-no">06</span>
</section>

</body>
</html>
```